KEV.PRO- Darren Holcombe Fitness- needs a clever business card using the logo, name, info, contact

I need a business card designed for my Online Personal Training company called KEV.PRO, abbreviation for Darren Holcombe Fitness. My company focuses on coaching in personal health and personal growth to unleash your greatest potential. I would like to see designs that use my color scheme of a redish-orange (C:0,M:84,Y:100,K:0), grey, white, black, and my company font is OSWALD. The final design should communicate some aspects of design, health, motivation, growth, in some way. The logo is very important to the company and can be displayed in any of the colors previously mentioned. Must include the company name, my website: www.kev-pro.example , my email: dan@kev-pro.example

Target Market(s)

Personal health, fitness, general public, those who lack knowledge, awareness, and confidence in personal health

Industry/Entity Type

Personal Trainer

Font styles to use
Other font styles liked:
• OSWALD. (Bold, Regular, Light)

Colors
f37122
ffffff
9d9d9d
000000

Requirements
Must have
• Must include the logo, company name, my website: www.kev-pro.example , my email: dan@kev-pro.example
Nice to have
• Variations of the colors scheme of a redish-orange (C:0,M:84,Y:100,K:0), grey, white, black. Logo, card, or text can be in any of these colors.
• Possible quote like "Take control of your personal health to unleash your greatest potential" or "Unleashing your greatness first begins with fitness of the body and mind"

```html
<!DOCTYPE html>
<html lang="en">
<head>
<meta charset="utf-8">
<title>KEV.PRO Business Card</title>
<link href="https://fonts.googleapis.com/css2?family=Oswald:wght@300;400;700&family=Work+Sans:wght@400;500&display=swap" rel="stylesheet">
<style>
  :root {
    --orange: #f15a24;
    --ink: #1d1e1e;
    --black: #000000;
    --white: #ffffff;
    --grey: #4a4a4a;
    --backdrop: #e6e6e6;
  }
  html, body {
    margin: 0;
    padding: 0;
    width: 1200px;
    height: 1000px;
    overflow: hidden;
    background: var(--backdrop);
  }
  .canvas {
    position: relative;
    width: 1200px;
    height: 1000px;
  }
  .card {
    position: absolute;
    left: 240px;
    width: 696px;
    height: 396px;
    border-radius: 18px;
    overflow: hidden;
  }
  .card--front { top: 83px; background: var(--white); }
  .card--back { top: 520px; background: var(--ink); }

  .brand-mark {
    position: absolute;
    display: flex;
    align-items: center;
    gap: 14px;
  }
  .brand-mark__dot {
    width: 26px;
    height: 26px;
    border-radius: 50%;
    background: var(--orange);
  }
  .brand-mark__name {
    font-family: 'Oswald', sans-serif;
    font-weight: 700;
    color: var(--orange);
    line-height: 1;
  }
  .card--front .brand-mark { left: 40px; top: 165px; }
  .card--front .brand-mark__name { font-size: 58px; }

  .contact {
    position: absolute;
    left: 435px;
    top: 80px;
    font-family: 'Work Sans', sans-serif;
    color: var(--grey);
  }
  .contact__name {
    margin: 0;
    font-size: 25px;
    font-weight: 400;
    letter-spacing: 1.5px;
    color: var(--orange);
    line-height: 1.2;
  }
  .contact__role {
    margin: 2px 0 0;
    font-size: 16px;
    font-weight: 500;
    color: #333;
  }
  .contact__rule {
    width: 32px;
    height: 2px;
    background: var(--orange);
    margin: 17px 0 30px;
  }
  .contact__address {
    margin: 0 0 28px;
    font-size: 15.5px;
    line-height: 20px;
  }
  .contact__list {
    list-style: none;
    margin: 0;
    padding: 0;
    font-size: 15.5px;
    line-height: 20px;
  }
  .contact__list li {
    display: flex;
    align-items: center;
    gap: 10px;
  }
  .contact__list svg { width: 10px; height: 10px; fill: var(--orange); }

  .front-band {
    position: absolute;
    left: 0;
    bottom: 0;
    width: 696px;
    height: 40px;
  }

  .card--back .brand-mark {
    left: 0;
    right: 0;
    top: 225px;
    flex-direction: column;
    gap: 4px;
  }
  .back-emblem {
    position: absolute;
    left: 283px;
    top: 60px;
    width: 130px;
    height: 130px;
    border-radius: 50%;
    background: var(--orange);
  }
  .card--back .brand-mark__name {
    font-size: 32px;
    color: var(--white);
  }
  .brand-mark__tagline {
    font-family: 'Oswald', sans-serif;
    font-weight: 400;
    font-size: 9.5px;
    letter-spacing: 0.3px;
    color: var(--white);
    text-transform: uppercase;
  }
  .back-quote {
    position: absolute;
    left: 0;
    right: 0;
    top: 345px;
    margin: 0;
    text-align: center;
    font-family: 'Oswald', sans-serif;
    font-weight: 400;
    font-size: 17px;
    color: var(--orange);
  }
</style>
</head>
<body>
<main class="canvas">

  <section class="card card--front" aria-label="Card front">
    <div class="brand-mark">
      <span class="brand-mark__dot"></span>
      <span class="brand-mark__name">KEV.PRO</span>
    </div>

    <div class="contact">
      <h1 class="contact__name">DAN HOLCOMBE</h1>
      <p class="contact__role">Trainer</p>
      <div class="contact__rule"></div>
      <p class="contact__address">418 Birchwood Road<br>Denver, CO 80203</p>
      <ul class="contact__list">
        <li><svg viewBox="0 0 10 10"><path d="M2 0h2l1 3-1.5 1a6 6 0 0 0 2.5 2.5L7 5l3 1v2c0 1-1 2-2 2C4 10 0 6 0 2 0 1 1 0 2 0z"/></svg>+1 555 014 2287</li>
        <li><svg viewBox="0 0 10 10"><path d="M0 2h10v6H0zM1 3v.3l4 2.6 4-2.6V3L5 5.5z" fill-rule="evenodd"/></svg>dan@kev-pro.example</li>
        <li><svg viewBox="0 0 10 10"><circle cx="5" cy="5" r="5"/></svg>www.kev-pro.example</li>
      </ul>
    </div>

    <svg class="front-band" viewBox="0 0 696 40" preserveAspectRatio="none" aria-hidden="true">
      <path d="M0 13 H400 Q412 13 404 19 L0 19 Z" fill="var(--black)"/>
      <path d="M0 21 H400 C425 21 430 4 470 4 H696 V40 H0 Z" fill="var(--orange)"/>
      <path d="M0 19 H404 L400 21 H0 Z" fill="var(--white)"/>
    </svg>
  </section>

  <section class="card card--back" aria-label="Card back">
    <span class="back-emblem"></span>
    <div class="brand-mark">
      <span class="brand-mark__name">KEV.PRO</span>
      <span class="brand-mark__tagline">Darren Holcombe Fitness</span>
    </div>
    <p class="back-quote">Take control of your personal health to unleash your greatest potential</p>
  </section>

</main>
</body>
</html>
```